High-end residential home builder needs a business card design

We need a new business card design for a small residential construction company based in Boise, Idaho. We specialize in building custom high-end homes and remodels, with a focus on great design and craftsmanship.

We would like to use our current logo, but open to new color suggestions.
Just looking for a clean, sharp, modern design that looks high-end.

Target Market(s)

Upscale clientele

Industry/Entity Type

Contractor

Contact Information for Business Card

Company: Stonefield Custom Builders
Name: Marcus Tilley
Phone number: 208 367 4120
Email: MarcusTilleySCB@mailbox-example.com
Website: Stonefieldcustombuilders-example.com

Font styles to use
Serif
Sans Serif

Requirements
Must have
• Company Logo
Company name
My name
My phone number
My email
Company website
Nice to have
• I have attached a few photos of cards that I really like.

```html
<!DOCTYPE html>
<html lang="en">
<head>
<meta charset="utf-8">
<title>Stonefield Custom Builders — Business Card</title>
<link rel="stylesheet" href="https://fonts.googleapis.com/css2?family=Montserrat:wght@500;600&family=Raleway:wght@400;500&display=swap">
<style>
  :root {
    --backdrop: #1b1b1c;
    --card-dark: #180d05;
    --card-mid: #2b1809;
    --card-warm: #341d0b;
    --accent: #e38b2f;
    --accent-soft: #c97a28;
    --shadow: rgba(0, 0, 0, 0.55);
  }
  * { margin: 0; padding: 0; box-sizing: border-box; }
  html, body {
    width: 1200px;
    height: 780px;
    overflow: hidden;
    background: var(--backdrop);
  }
  .canvas {
    position: relative;
    width: 1200px;
    height: 780px;
  }
  .card {
    position: absolute;
    width: 520px;
    height: 297px;
    box-shadow: 0 14px 30px var(--shadow);
    overflow: hidden;
  }

  /* Front: personal details */
  .card-front {
    left: 80px;
    top: 80px;
    background: linear-gradient(200deg, var(--card-dark) 0%, var(--card-mid) 55%, var(--card-warm) 100%);
  }
  .person-name {
    position: absolute;
    left: 40px;
    top: 46px;
    font-family: "Montserrat", sans-serif;
    font-weight: 600;
    font-size: 22px;
    letter-spacing: 0.2em;
    color: var(--accent);
    text-transform: uppercase;
  }
  .person-role {
    position: absolute;
    left: 42px;
    top: 80px;
    font-family: "Raleway", sans-serif;
    font-weight: 400;
    font-size: 11px;
    letter-spacing: 0.3em;
    color: var(--accent-soft);
    text-transform: uppercase;
  }
  .contact-list {
    position: absolute;
    left: 42px;
    bottom: 34px;
    display: grid;
    grid-template-columns: 70px auto;
    row-gap: 3px;
    font-family: "Raleway", sans-serif;
    font-weight: 500;
    font-size: 12px;
    color: var(--accent);
  }
  .contact-label { color: var(--accent-soft); }
  .front-brand {
    position: absolute;
    right: 34px;
    top: 132px;
    display: flex;
    align-items: center;
    gap: 8px;
    font-family: "Montserrat", sans-serif;
    font-weight: 500;
    font-size: 11px;
    letter-spacing: 0.2em;
    color: var(--accent);
    text-transform: uppercase;
  }
  .brand-square {
    width: 10px;
    height: 10px;
    border: 1.5px solid var(--accent);
  }

  /* Back: company side */
  .card-back {
    left: 600px;
    top: 403px;
  }
  .pattern-field {
    position: absolute;
    inset: 0;
    background: radial-gradient(ellipse at 50% 45%, var(--card-warm) 0%, var(--card-mid) 55%, var(--card-dark) 100%);
  }
  .back-brand {
    position: absolute;
    inset: 0;
    display: flex;
    flex-direction: column;
    align-items: center;
    justify-content: center;
    gap: 14px;
  }
  .back-brand .brand-square {
    width: 22px;
    height: 22px;
    border-width: 2px;
  }
  .company-name {
    font-family: "Montserrat", sans-serif;
    font-weight: 500;
    font-size: 17px;
    letter-spacing: 0.28em;
    color: var(--accent);
    text-transform: uppercase;
    text-align: center;
  }
</style>
</head>
<body>
<main class="canvas">
  <section class="card card-front">
    <h1 class="person-name">Marcus Tilley</h1>
    <p class="person-role">Designation</p>
    <div class="front-brand">
      <span class="brand-square"></span>
      <span>Stonefield</span>
    </div>
    <dl class="contact-list">
      <dt class="contact-label">Phone</dt><dd>208 367 4120</dd>
      <dt class="contact-label">Email</dt><dd>MarcusTilleySCB@mailbox-example.com</dd>
      <dt class="contact-label">Website</dt><dd>Stonefieldcustombuilders-example.com</dd>
    </dl>
  </section>

  <section class="card card-back">
    <div class="pattern-field" role="img" aria-label="Subtle tone-on-tone repeating hexagon pattern in dark brown"></div>
    <div class="back-brand">
      <span class="brand-square"></span>
      <p class="company-name">Stonefield Custom Builders</p>
    </div>
  </section>
</main>
</body>
</html>
```